Business Card

We need some ideas for corporate business cards. I'm interested in a double sided card, with one side featuring our corporate logo, the other side with employee information.

Corporate colors, logo etc. available at www.varnik.com

Industry/Entity Type

Business

Requirements
Must have
• The "Varnik" logo with stylized "O"

Nice to have
• Preferred font is calibri

```html
<!DOCTYPE html>
<html lang="en">
<head>
<meta charset="UTF-8">
<title>Varnik Business Card</title>
<link href="https://fonts.googleapis.com/css2?family=Carlito:wght@400;700&display=swap" rel="stylesheet">
<style>
  :root {
    --bg: #d9dadb;
    --card: #fafafa;
    --teal: #0b6470;
    --grey-band: #bdbebf;
    --grey-mark: #b3b3b3;
    --white: #ffffff;
  }
  * { margin: 0; padding: 0; box-sizing: border-box; }
  html, body {
    width: 1200px; height: 1000px; overflow: hidden;
    background: var(--bg);
    font-family: "Carlito", "Calibri", sans-serif;
  }
  .canvas {
    position: relative; width: 1200px; height: 1000px;
    display: flex; flex-direction: column; align-items: center; justify-content: center; gap: 50px;
  }
  .card {
    position: relative; width: 700px; height: 400px;
    background: var(--card);
    box-shadow: 0 6px 18px rgba(0,0,0,0.18);
    overflow: hidden;
  }
  /* Front: employee information */
  .person { position: absolute; left: 470px; top: 70px; color: var(--teal); }
  .person-name { font-size: 31px; font-weight: 700; line-height: 1; }
  .person-role { font-size: 18px; font-weight: 400; margin-top: 2px; }

  .brand {
    position: absolute; left: 40px; top: 258px;
    display: flex; align-items: center; gap: 14px;
    color: var(--teal);
  }
  .brand-square { width: 30px; height: 30px; background: var(--teal); }
  .brand-name { font-size: 60px; font-weight: 700; letter-spacing: 6px; line-height: 1; }

  .divider { position: absolute; left: 428px; top: 250px; width: 3px; height: 82px; background: var(--teal); }

  .contact { position: absolute; left: 458px; top: 248px; color: var(--teal); font-size: 20px; line-height: 27px; list-style: none; white-space: nowrap; }
  .contact-label { display: inline-block; width: 36px; }

  .footer-band { position: absolute; left: 0; bottom: 0; width: 700px; height: 48px; }
  .website {
    position: absolute; right: 0; bottom: 0; width: 265px; height: 48px;
    display: flex; align-items: center; padding-left: 30px;
    color: var(--white); font-size: 20px;
  }

  /* Back: corporate identity */
  .card-back { display: flex; align-items: center; justify-content: center; }
  .back-brand { display: flex; align-items: center; gap: 24px; color: var(--grey-mark); }
  .back-square { width: 70px; height: 70px; background: var(--grey-mark); }
  .back-name { font-size: 110px; font-weight: 700; letter-spacing: 8px; line-height: 1; }
</style>
</head>
<body>
<main class="canvas">
  <section class="card card-front">
    <div class="person">
      <p class="person-name">Person Name</p>
      <p class="person-role">designation</p>
    </div>

    <div class="brand">
      <span class="brand-square"></span>
      <span class="brand-name">VARNIK</span>
    </div>

    <div class="divider"></div>

    <ul class="contact">
      <li><span class="contact-label">P :</span>555 0142 3861</li>
      <li><span class="contact-label">F :</span>555 0142 3861</li>
      <li><span class="contact-label">E :</span>hello@varnikmail.com</li>
    </ul>

    <svg class="footer-band" viewBox="0 0 700 48" width="700" height="48" aria-hidden="true">
      <polygon points="0,0 425,0 450,48 0,48" fill="var(--teal)"/>
      <polygon points="425,0 700,0 700,48 450,48" fill="var(--grey-band)"/>
    </svg>
    <div class="website">www.varnik.com</div>
  </section>

  <section class="card card-back">
    <div class="back-brand">
      <span class="back-square"></span>
      <span class="back-name">VARNIK</span>
    </div>
  </section>
</main>
</body>
</html>
```